Up to the ASCENT - PPT Template with Splash Slide

We are looking for a PPT template that has 4 slides.
1. Splash slide (Creative, fun, no content, a visual representation of the theme)
2. Section header slide
3. Content Slide
4. Content Slide, another design option
The theme is 'UP to the ASCENT'. The design should reflect this theme.
The colors should be in Purple (#864B99), Blue (#0A80C2), and Green (#52B054).

```html
<!DOCTYPE html>
<html lang="en">
<head>
<meta charset="utf-8">
<title>Presentation Template – Slide Overview</title>
<link href="https://fonts.googleapis.com/css2?family=Montserrat:wght@700;800&family=Lato:wght@400;700&display=swap" rel="stylesheet">
<style>
  :root {
    --purple: #864B99;
    --blue: #0A80C2;
    --green: #52B054;
    --stage: #5f5f5f;
    --ink: #1d1d1f;
    --body: #3a3a3a;
    --white: #ffffff;
    --faint: #efe8f3;
  }
  * { margin: 0; padding: 0; box-sizing: border-box; }
  html, body { width: 1200px; height: 367px; overflow: hidden; background: var(--stage); }
  .board { position: relative; width: 1200px; height: 367px; }
  .slide {
    position: absolute; width: 283px; height: 159px; background: var(--white);
    overflow: hidden; font-family: "Lato", sans-serif; color: var(--body);
  }
  .col-1 { left: 15px; } .col-2 { left: 312px; } .col-3 { left: 608px; } .col-4 { left: 905px; }
  .row-1 { top: 14px; } .row-2 { top: 190px; }

  .bar { position: absolute; left: 0; bottom: 0; width: 100%; height: 2px;
    background: linear-gradient(90deg, var(--blue) 73%, var(--purple) 73%); }
  .foot { position: absolute; bottom: 8px; font-size: 3.3px; color: var(--blue); }
  .foot-date { left: 14px; } .foot-page { right: 14px; }
  .on-dark .foot { color: var(--white); }

  .photo { position: absolute; }
  .photo-sky { inset: 0; background: linear-gradient(180deg, #9aa2b4 0%, #c3c6cf 45%, #e8e1d4 70%, #55575a 82%, #101010 100%); }
  .photo-maze { inset: 0; background: radial-gradient(circle at 48% 38%, #d8d9db 0%, #7c7f84 25%, #3e4146 60%, #24262a 100%); }

  .section-title { position: absolute; left: 0; right: 0; top: 64px; text-align: center;
    font-family: "Montserrat", sans-serif; font-weight: 800; font-size: 16px; color: var(--purple); letter-spacing: 0.2px; }
  .bg-ring { position: absolute; left: 83px; top: 22px; width: 118px; height: 118px; border-radius: 50%; border: 9px solid var(--faint); }

  .heading { position: absolute; left: 14px; top: 10px; font-family: "Montserrat", sans-serif; font-weight: 800; font-size: 7px; color: var(--blue); }
  .brand { position: absolute; top: 9px; display: flex; align-items: center; gap: 2px;
    font-family: "Montserrat", sans-serif; font-weight: 800; font-size: 8px; color: var(--ink); }
  .brand-dot { width: 8px; height: 8px; border-radius: 50%; border: 1.4px solid var(--purple); }
  .brand-right { right: 13px; } .brand-left { left: 14px; }

  .copy { position: absolute; font-size: 3.3px; line-height: 7.05px; text-align: justify; color: var(--body); }
  .copy p + p { margin-top: 7px; }

  .purple-panel { position: absolute; left: 207px; top: 0; width: 76px; height: 159px; background: linear-gradient(135deg, #7d3f93, #9a5cb0); }
  .photo-team { left: 142px; top: 27px; width: 127px; height: 104px; border-radius: 14px;
    background: radial-gradient(circle at 55% 50%, #d9d7d0 0%, #8e8c88 55%, #6f6e6b 100%); }
  .about-title { position: absolute; left: 14px; top: 38px; font-family: "Montserrat", sans-serif; font-weight: 800; font-size: 7px; color: var(--blue); }
  .about-copy { position: absolute; left: 14px; width: 118px; font-size: 3.2px; line-height: 7px; }
  .ticks { position: absolute; left: 14px; top: 95px; list-style: none; font-size: 3.2px; }
  .ticks li { display: flex; align-items: center; gap: 3px; height: 11px; }
  .ticks li::before { content: ""; width: 4px; height: 4px; border-radius: 50%; border: 0.8px solid var(--purple); }

  .photo-chess { inset: 0; background: linear-gradient(90deg, #fafafa 0%, #f0f0f1 50%, #e4e5e7 100%); }
  .contact-brand { position: absolute; left: 27px; top: 58px; display: flex; align-items: center; gap: 4px;
    font-family: "Montserrat", sans-serif; font-weight: 800; font-size: 14.5px; color: var(--ink); }
  .contact-brand .brand-dot { width: 14px; height: 14px; border-width: 2.2px; }
  .thanks { position: absolute; left: 45px; width: 80px; top: 91px; text-align: center; font-family: "Montserrat", sans-serif; font-weight: 700; font-size: 8px; color: var(--ink); }
  .divider { position: absolute; left: 165px; top: 34px; width: 0.5px; height: 83px; background: #d5d5d8; }
  .contact-item { position: absolute; left: 184px; display: flex; align-items: center; gap: 6px; }
  .contact-icon { width: 14px; height: 14px; border-radius: 50%; background: linear-gradient(135deg, var(--blue), var(--purple)); display: flex; align-items: center; justify-content: center; }
  .contact-label { font-size: 2.4px; font-weight: 700; color: var(--ink); }
  .contact-value { font-size: 4.4px; font-weight: 700; color: var(--ink); margin-top: 1px; }
</style>
</head>
<body>
<main class="board">

  <section class="slide col-1 row-1">
    <div class="photo photo-sky" role="img" aria-label="Silhouette of a person leaping across a gap between two cliffs against a cloudy sky"></div>
  </section>

  <section class="slide col-2 row-1">
    <div class="bg-ring"></div>
    <h1 class="section-title">INTRODUCTION</h1>
    <span class="foot foot-date">13 May 2024</span><span class="foot foot-page">Page No: 02</span>
    <div class="bar"></div>
  </section>

  <section class="slide col-3 row-1">
    <h2 class="heading">WHY CHOOSE US</h2>
    <div class="brand brand-right"><span class="brand-dot"></span>ASCENT</div>
    <div class="copy" style="left:14px;top:27px;width:75px">Nam libero tempore, cum soluta nobis est eligendi optio cumque nihil impedit quo minus id quod maxime placeat facere possimus, omnis voluptas assumenda est, omnis dolor repellendus. Temporibus autem quibusdam et aut officiis debitis aut rerum necessitatibus saepe eveniet ut et voluptates repudiandae sint et molestiae non recusandae. Itaque earum rerum hic tenetur a sapiente delectus, ut aut reiciendis voluptatibus maiores aut officiis debitis aut rerum necessitatibus saepe eveniet ut et voluptates repudiandae sint aut officiis debitis aut rerum necessitatibus aut officiis debitis aut rerum necessitatibus alias consequatur aut perferendis doloribus asperiores repellat.</div>
    <div class="copy" style="left:104px;top:27px;width:75px">Libero tempore, cum soluta nobis est eligendi optio cumque nihil impedit quo minus id quod maxime placeat facere possimus, omnis voluptas assumenda est, omnis dolor repellendus. Temporibus autem quibusdam et aut officiis debitis aut rerum necessitatibus saepe eveniet ut et voluptates repudiandae sint et molestiae non recusandae. Itaque earum rerum hic tenetur a sapiente delectus, ut aut reiciendis voluptatibus maiores aut officiis debitis aut rerum necessitatibus saepe eveniet ut et voluptates repudiandae sint aut officiis debitis aut rerum necessitatibus aut officiis debitis aut rerum necessitatibus alias consequatur aut perferendis doloribus asperiores repellat.</div>
    <div class="copy" style="left:194px;top:27px;width:75px">Tempore, cum soluta nobis est eligendi optio cumque nihil impedit quo minus id quod maxime placeat facere possimus, omnis voluptas assumenda est, omnis dolor repellendus. Temporibus autem quibusdam et aut officiis debitis aut rerum necessitatibus saepe eveniet ut et voluptates repudiandae sint et molestiae non recusandae. Itaque earum rerum hic tenetur a sapiente delectus, ut aut reiciendis voluptatibus maiores aut officiis debitis aut rerum necessitatibus saepe eveniet ut et voluptates repudiandae sint aut officiis debitis aut rerum necessitatibus aut officiis debitis aut rerum necessitatibus alias consequatur aut perferendis doloribus asperiores repellat.</div>
    <span class="foot foot-date">13 May 2024</span><span class="foot foot-page">Page No: 03</span>
    <div class="bar"></div>
  </section>

  <section class="slide col-4 row-1 on-dark">
    <div class="purple-panel"></div>
    <div class="photo photo-team" role="img" aria-label="Team seen from above joining large puzzle pieces on a grey floor"></div>
    <div class="brand brand-left"><span class="brand-dot"></span>ASCENT</div>
    <h2 class="about-title">ABOUT ASCENT</h2>
    <p class="about-copy" style="top:50px">Temporibus autem quibusdam et aut officiis debitis aut rerum necessit niet ut et voluptates repudiandae sint et molestiae non recusandae.</p>
    <p class="about-copy" style="top:71px">Itaque earum rerum hic tenetur a sapiente delectus, ut aut reiciendis voluptatibus maiores alias consequatur aut perferendis doloribus asperiores repellat.</p>
    <ul class="ticks">
      <li>Nam libero tempore, cum soluta nobis est eligendi</li>
      <li>At vero eos et accusamus et iusto odio dignissimos ducimus</li>
      <li>Voluptatibus maiores alias consequatur aut perferendis</li>
    </ul>
    <span class="foot foot-date" style="color:var(--blue)">13 May 2024</span><span class="foot foot-page">Page No: 04</span>
    <div class="bar"></div>
  </section>

  <section class="slide col-1 row-2 on-dark">
    <div class="photo photo-maze" role="img" aria-label="Red ball smashing a straight path through the walls of a grey maze"></div>
    <span class="foot foot-date">13 May 2024</span><span class="foot foot-page">Page No: 05</span>
    <div class="bar"></div>
  </section>

  <section class="slide col-2 row-2">
    <div class="bg-ring"></div>
    <h1 class="section-title" style="top:73px">OUR BENEFITS</h1>
    <span class="foot foot-date">13 May 2024</span><span class="foot foot-page">Page No: 06</span>
    <div class="bar"></div>
  </section>

  <section class="slide col-3 row-2">
    <h2 class="heading">OUR BENEFITS</h2>
    <div class="brand brand-right"><span class="brand-dot"></span>ASCENT</div>
    <div class="copy" style="left:14px;top:28px;width:120px">
      <p>Nam libero tempore, cum soluta nobis est eligendi optio cumque nihil impedit quo minus id quod maxime placeat facere possimus, omnis voluptas assumenda est, omnis dolor repellendus. Temporibus autem quibusdam et aut officiis debitis aut rerum necessitatibus saepe eveniet ut et voluptates repudiandae sint et molestiae non recusandae. Itaque earum rerum hic tenetur a sapiente delectus, ut aut reiciendis voluptatibus maiores aut officiis debitis aut rerum necessitatibus saepe eveniet ut et voluptates repudiandae sint aut officiis debitis aut rerum necessitatibus aut officiis debitis aut rerum necessitatibus alias consequatur aut perferendis doloribus asperiores repellat.</p>
      <p>At vero eos et accusamus et iusto odio dignissimos ducimus qui blanditiis praesentium voluptatum deleniti atque corrupti quos dolores et quas excepturi sint occaecati cupiditate non provident, similique sunt in culpa qui molestias excepturi sint occaecati cupiditate non provident, similique sunt in culpa qui officia deserunt mollitia animi, id est laborum et dolorum fuga.</p>
    </div>
    <div class="copy" style="left:149px;top:28px;width:120px">
      <p>Tempore, cum soluta nobis est eligendi optio cumque nihil impedit quo minus id quod maxime placeat facere possimus, omnis voluptas assumenda est, omnis dolor repellendus. Temporibus autem quibusdam et aut officiis debitis aut rerum necessitatibus saepe eveniet ut et voluptates repudiandae sint et molestiae non recusandae. Itaque earum rerum hic tenetur a sapiente delectus, ut aut reiciendis voluptatibus maiores aut officiis debitis aut rerum necessitatibus saepe eveniet ut et voluptates repudiandae sint aut officiis debitis aut rerum necessitatibus aut officiis debitis aut rerum necessitatibus alias consequatur aut perferendis doloribus asperiores repellat.</p>
      <p>At vero eos et accusamus et iusto odio dignissimos ducimus qui blanditiis praesentium voluptatum deleniti atque corrupti quos dolores et quas molestias excepturi sint occaecati cupiditate non provident, similique sunt in culpa qui officia deserunt mollitia animi, id est laborum et dolorum fuga, similique sunt in culpa.</p>
    </div>
    <span class="foot foot-date">13 May 2024</span><span class="foot foot-page">Page No: 07</span>
    <div class="bar"></div>
  </section>

  <section class="slide col-4 row-2">
    <div class="photo photo-chess" role="img" aria-label="Faded black and white chess pieces on a board"></div>
    <h2 class="heading">CONTACT US</h2>
    <div class="contact-brand"><span class="brand-dot"></span>ASCENT</div>
    <p class="thanks">THANK YOU</p>
    <div class="divider"></div>
    <div class="contact-item" style="top:37px">
      <span class="contact-icon"><svg width="6" height="6" viewBox="0 0 24 24"><path fill="#fff" d="M6.6 10.8a15 15 0 0 0 6.6 6.6l2.2-2.2a1 1 0 0 1 1-.25 11.4 11.4 0 0 0 3.6.57 1 1 0 0 1 1 1V20a1 1 0 0 1-1 1A17 17 0 0 1 3 4a1 1 0 0 1 1-1h3.5a1 1 0 0 1 1 1c0 1.250.2 2.45.57 3.6a1 1 0 0 1-.25 1z"/></svg></span>
      <div><div class="contact-label">PHONE NUMBER:</div><div class="contact-value">+1 555 010 2040</div></div>
    </div>
    <div class="contact-item" style="top:69px">
      <span class="contact-icon"><svg width="6" height="6" viewBox="0 0 24 24"><path fill="#fff" d="M3 5h18a1 1 0 0 1 1 1v12a1 1 0 0 1-1 1H3a1 1 0 0 1-1-1V6a1 1 0 0 1 1-1zm9 7 8.5-5.5H3.5z"/></svg></span>
      <div><div class="contact-label">MAIL US:</div><div class="contact-value">hello@ascent-studio.example</div></div>
    </div>
    <div class="contact-item" style="top:100px">
      <span class="contact-icon"><svg width="6" height="6" viewBox="0 0 24 24"><path fill="#fff" d="M12 2a7 7 0 0 1 7 7c0 5-7 13-7 13S5 14 5 9a7 7 0 0 1 7-7zm0 4.5A2.5 2.5 0 1 0 12 11.5 2.5 2.5 0 0 0 12 6.5z"/></svg></span>
      <div><div class="contact-label">LOCATION:</div><div class="contact-value">Ascent, United States</div></div>
    </div>
    <span class="foot foot-date">13 May 2024</span><span class="foot foot-page">Page No: 08</span>
    <div class="bar"></div>
  </section>

</main>
</body>
</html>
```